Mbeleko & Tumusiime Advocates website

An interactive professional law firm website fully synchronized with social media pages.

Target Market(s)

Corporations and professionals

Industry/Entity Type

Professional Service

Number of Pages Required

5+ page

Font styles to use
Sans Serif

Colors

Designer to choose colors to be used in the design.

```html
<!DOCTYPE html>
<html lang="en">
<head>
<meta charset="utf-8">
<title>Mbeleko &amp; Tumusiime Advocates</title>
<link rel="stylesheet" href="https://fonts.googleapis.com/css2?family=Playfair+Display:wght@400;700&family=Montserrat:wght@400;500;600&display=swap">
<style>
:root{
  --red:#b31b2c;
  --navy:#23416a;
  --navy-card:#2f5180;
  --ink:#2b2b2b;
  --muted:#6d6d6d;
  --light:#f3f3f3;
  --dark:#3a3a3a;
  --white:#ffffff;
  --line:#d9d9d9;
  --serif:"Playfair Display", Georgia, serif;
  --sans:"Montserrat", Arial, sans-serif;
}
*{box-sizing:border-box;margin:0;padding:0}
html,body{width:1200px;height:4369px;overflow:hidden}
body{font-family:var(--sans);color:var(--ink);background:var(--white);position:relative}
section,header,footer{position:absolute;left:0;width:1200px}
.label{font-size:11px;color:var(--red);font-weight:500}
.title{font-family:var(--serif);font-weight:400;color:var(--ink)}
.btn{display:inline-block;font-size:11px;padding:9px 16px;border:1px solid var(--red);color:var(--red);background:var(--white)}
.btn-solid{background:var(--red);color:var(--white)}
.photo{position:absolute}

/* header */
.site-header{top:0;height:82px;background:var(--white);border-bottom:1px solid #eee}
.brand{position:absolute;left:80px;top:20px;display:flex;align-items:center;gap:10px}
.brand-square{width:30px;height:30px;background:var(--red)}
.brand-name{font-family:var(--serif);font-size:16px;line-height:18px;color:var(--ink);width:170px}
.top-contact{position:absolute;right:80px;top:10px;display:flex;align-items:center;gap:16px;font-size:13px}
.top-contact b{color:var(--red);font-weight:600}
.top-contact .btn{padding:6px 14px}
.main-nav{position:absolute;right:80px;top:50px;display:flex;gap:26px;font-size:12px}
.main-nav a{color:var(--ink);text-decoration:none}
.main-nav a.active{color:var(--red);border-bottom:1px solid var(--red);padding-bottom:3px}

/* hero */
.hero{top:82px;height:477px}
.hero .photo{inset:0;background:linear-gradient(180deg,#6d5a4a 0%,#3d3129 55%,#231c17 100%)}
.hero-title{position:absolute;top:120px;width:100%;text-align:center;font-family:var(--serif);font-size:32px;color:var(--white)}
.hero-tagline{position:absolute;top:214px;left:300px;width:600px;text-align:center;color:var(--white);font-size:15px;line-height:21px;background:rgba(0,0,0,.35);padding:8px 20px}
.hero .btn{position:absolute;top:294px;left:550px;width:100px;text-align:center;padding:7px 0}
.arrow{position:absolute;top:225px}

/* history */
.history{top:559px;height:426px}
.history .photo{left:0;top:0;width:533px;height:426px;background:linear-gradient(135deg,#9c1b27 0%,#5a1a20 45%,#2a2628 100%)}
.history-body{position:absolute;left:612px;top:60px;width:430px}
.history-body .title{font-size:24px;margin:8px 0 18px}
.history-body p{font-size:11px;line-height:16px;color:var(--muted);margin-bottom:12px}
.history-body .btn{margin-top:10px}

/* stats */
.stats{top:985px;height:195px;background:var(--navy);display:flex;justify-content:center}
.stat{width:230px;text-align:center;color:var(--white);padding-top:52px;border-left:1px solid rgba(255,255,255,.18)}
.stat:first-child{border-left:none}
.stat p{font-size:14px;font-weight:600;margin-top:14px;line-height:18px}

/* who we are */
.who{top:1180px;height:428px}
.who .photo{left:665px;top:0;width:535px;height:428px;background:linear-gradient(160deg,#d8d4cc 0%,#9c8a6e 55%,#4a3a2a 100%)}
.who-body{position:absolute;left:155px;top:65px;width:470px}
.who-body .title{font-size:30px;margin:6px 0 14px}
.who-body > p{font-size:11px;line-height:16px;color:var(--muted)}
.cols{display:flex;gap:30px;margin-top:30px}
.cols div{width:210px}
.cols h4{font-size:13px;font-weight:600;margin-bottom:8px}
.cols p{font-size:11px;line-height:16px;color:var(--muted)}
.who-actions{display:flex;align-items:center;gap:18px;margin-top:50px;font-size:13px}
.who-actions b{color:var(--red);font-weight:600}

/* practice */
.practice{top:1608px;height:533px;background:var(--navy);text-align:center}
.practice .eyebrow{font-size:11px;color:var(--white);margin-top:64px}
.practice .title{color:var(--white);font-size:30px;margin-top:4px}
.cards{position:absolute;top:134px;left:155px;display:flex;gap:22px}
.card{width:285px;height:312px;background:var(--navy-card)}
.card .photo{position:relative;height:160px}
.card h3{font-size:16px;font-weight:500;color:var(--white);margin:16px 0 8px}
.card p{font-size:11px;line-height:16px;color:#cfd9e6;padding:0 30px}
.card .btn{margin-top:14px;border-color:var(--white);background:transparent;color:var(--white);padding:6px 14px}
.card .btn.on{background:var(--white);color:var(--navy)}

/* how */
.how{top:2141px;height:452px;text-align:center}
.how .label{margin-top:56px}
.how .title{font-size:30px;margin-top:2px}
.values{position:absolute;top:140px;left:160px;width:880px;display:flex;justify-content:space-between}
.value{width:260px}
.ring{width:84px;height:84px;border-radius:50%;border:1px solid var(--red);margin:0 auto;display:flex;align-items:center;justify-content:center}
.ring.on{background:var(--red)}
.value h3{font-size:16px;font-weight:500;margin:22px 0 10px}
.value p{font-size:11px;line-height:16px;color:var(--muted)}
.how-rule{position:absolute;top:364px;left:470px;width:260px;border-top:1px solid var(--red)}
.how .btn{position:absolute;top:350px;left:532px;padding:7px 16px}

/* clients */
.clients{top:2593px;height:335px;background:var(--light);text-align:center}
.clients .title{font-size:30px;margin-top:50px}
.tabs{position:absolute;top:118px;left:160px;width:880px;display:flex;justify-content:space-around;font-size:13px;border-bottom:1px solid var(--line)}
.tabs span{padding-bottom:12px}
.tabs .on{color:var(--red);border-bottom:2px solid var(--red)}
.logos{position:absolute;top:188px;left:180px;width:840px;display:flex;justify-content:space-between;align-items:center}
.logo{width:150px;height:80px;display:flex;align-items:center;justify-content:center;font-size:22px;font-weight:600;color:#555}
.logo.on{background:var(--white);box-shadow:0 2px 8px rgba(0,0,0,.12)}

/* professionals */
.team{top:2928px;height:591px;text-align:center}
.team .label{margin-top:60px}
.team .title{font-size:30px;margin-top:2px}
.members{position:absolute;top:145px;left:163px;display:flex;gap:36px}
.member{width:190px;height:315px;background:var(--white);box-shadow:0 1px 6px rgba(0,0,0,.12)}
.member .photo{position:relative;height:233px;background:linear-gradient(180deg,#d9d9d9 0%,#9a9a9a 100%)}
.member .info{height:82px;padding-top:22px}
.member h4{font-size:13px;font-weight:600}
.member span{font-size:11px;color:var(--muted)}
.member.on .info{background:var(--red)}
.member.on h4,.member.on span{color:var(--white)}
.team .btn{position:absolute;top:505px;left:550px;padding:8px 16px}

/* contact */
.contact{top:3519px;height:428px;background:var(--dark);color:var(--white)}
.contact .eyebrow{text-align:center;font-size:11px;margin-top:66px}
.contact .title{text-align:center;color:var(--white);font-size:30px}
.info-col{position:absolute;left:218px;top:156px;width:240px;font-size:12px;line-height:17px}
.info-col h3{font-size:16px;font-weight:500;margin-bottom:12px}
.info-col h4{font-size:12px;font-weight:600;margin-top:12px}
.form-col{position:absolute;left:480px;top:156px;width:500px}
.form-col h3{font-size:16px;font-weight:500;margin-bottom:12px}
.fields{display:flex;gap:20px}
.field{flex:1;border-bottom:1px solid #777;font-size:11px;color:#bbb;padding-bottom:8px}
.area{margin-top:20px;height:80px;border-bottom:1px solid #777;font-size:11px;color:#bbb}
.form-col .btn{margin-top:24px;background:transparent;border-color:var(--white);color:var(--white);padding:6px 20px}

/* map */
.map{top:3947px;height:271px;background:linear-gradient(135deg,#e9e9e6 0%,#dadad6 100%)}

/* footer */
.site-footer{top:4218px;height:151px;background:var(--white)}
.site-footer .brand{top:32px}
.foot-nav{position:absolute;right:80px;top:46px;display:flex;gap:26px;font-size:12px}
.foot-nav .active{color:var(--red);border-bottom:1px solid var(--red)}
.foot-bottom{position:absolute;left:80px;right:80px;top:100px;border-top:1px solid var(--line);padding-top:16px;display:flex;justify-content:space-between;font-size:11px;color:var(--muted)}
.social{display:flex;align-items:center;gap:8px;color:var(--ink)}
.social i{width:20px;height:20px;border-radius:50%;background:var(--red);display:inline-block}
</style>
</head>
<body>

<header class="site-header">
  <div class="brand">
    <div class="brand-square"></div>
    <div class="brand-name">Mbeleko &amp; Tumusiime Advocates</div>
  </div>
  <div class="top-contact">
    <span>Call Us: <b>0414 555 018</b></span>
    <span class="btn btn-solid">Free Consultation</span>
  </div>
  <nav class="main-nav">
    <a class="active">Home</a><a>Our History</a><a>Who We Are</a><a>How We Do It</a><a>Practice Areas</a><a>Our clients</a><a>Our Professionals</a><a>Contact Us</a>
  </nav>
</header>

<section class="hero">
  <div class="photo" role="img" aria-label="Law library with a judge's gavel on a desk"></div>
  <h1 class="hero-title">Mbeleko &amp; Tumusiime Advocates</h1>
  <p class="hero-tagline">To provide legal services focused on commercial litigation, construction law and arbitration with efficiency, integrity and client satisfaction.</p>
  <span class="btn btn-solid">Explore More</span>
  <svg class="arrow" style="left:78px" width="16" height="28" viewBox="0 0 16 28"><path d="M13 2 2 14l11 12" fill="none" stroke="#fff" stroke-width="2.5"/></svg>
  <svg class="arrow" style="left:1106px" width="16" height="28" viewBox="0 0 16 28"><path d="M3 2l11 12L3 26" fill="none" stroke="#fff" stroke-width="2.5"/></svg>
</section>

<section class="history">
  <div class="photo" role="img" aria-label="Group portrait of the firm's partners and staff"></div>
  <div class="history-body">
    <div class="label">Our History</div>
    <h2 class="title">Mbeleko &amp; Tumusiime Advocates</h2>
    <p>In 1966, our firm was founded and is comprised of 5 Partners and over 15 Associates and support staff fully engaged and focused on client service. The firm is fully automated and is run on the latest practice management software with efficient client focused delivery systems and improved turn around times.</p>
    <p>Over the years, the firm has worked with the international firm of Harcourt Lyle in successfully representing clients internationally against a multimillion dollar lawsuit and has acted for both ...</p>
    <span class="btn">Discover More About</span>
  </div>
</section>

<section class="stats">
  <div class="stat">
    <svg width="40" height="30" viewBox="0 0 40 30"><circle cx="14" cy="8" r="6" fill="#fff"/><circle cx="28" cy="9" r="5" fill="#fff"/><path d="M2 28c0-8 6-12 12-12s12 4 12 12z M24 28c0-5 2-9 4-10 5 0 10 3 10 10z" fill="#fff"/></svg>
    <p>5 - PARTNERS</p>
  </div>
  <div class="stat">
    <svg width="40" height="30" viewBox="0 0 40 30"><circle cx="12" cy="9" r="5" fill="#fff"/><circle cx="28" cy="9" r="5" fill="#fff"/><path d="M2 28c0-7 5-11 10-11s10 4 10 11zM18 28c0-7 5-11 10-11s10 4 10 11z" fill="#fff"/></svg>
    <p>20+ PEOPLE</p>
  </div>
  <div class="stat">
    <svg width="32" height="32" viewBox="0 0 32 32"><rect x="3" y="6" width="26" height="23" fill="none" stroke="#fff" stroke-width="2.5"/><path d="M3 12h26M10 3v6M22 3v6" stroke="#fff" stroke-width="2.5"/></svg>
    <p>55 YEARS OF COMBINED<br>EXPERIENCE</p>
  </div>
  <div class="stat">
    <svg width="32" height="32" viewBox="0 0 32 32"><path d="M4 14h6v15H4zM12 14l6-11c3 0 4 2 3 5l-1 5h8c2 0 3 2 2 4l-3 10c-1 2-2 2-4 2H12z" fill="#fff"/></svg>
    <p>350+ CASES SOLVED</p>
  </div>
</section>

<section class="who">
  <div class="who-body">
    <div class="label">Mbeleko &amp; Tumusiime</div>
    <h2 class="title">Who We Are</h2>
    <p>Mbeleko &amp; Tumusiime Advocates are a specialist commercial law firm in Uganda focusing on commercial litigation, construction law and arbitration. We have excelled in our niche areas for over two decades and we continue to grow and be the firm choice in those practice areas.</p>
    <div class="cols">
      <div><h4>Vision</h4><p>To be the firm of choice in our niche practice areas of commercial law.</p></div>
      <div><h4>Mission</h4><p>To provide legal services focused on commercial litigation, construction law and arbitration with efficiency, integrity and client satisfaction.</p></div>
    </div>
    <div class="who-actions"><span class="btn">Free Consultation</span><span>Call Us: <b>0414 555 018</b></span></div>
  </div>
  <div class="photo" role="img" aria-label="Gavel and scales of justice on a desk"></div>
</section>

<section class="practice">
  <div class="eyebrow">What We Do</div>
  <h2 class="title">Practice Areas</h2>
  <div class="cards">
    <div class="card">
      <div class="photo" role="img" aria-label="Hard hat and construction tools" style="background:linear-gradient(135deg,#e7c22a,#6a5a2a)"></div>
      <h3>Construction Law</h3>
      <p>Our Construction Law department is headed by our Senior Partner Daniel Mbeleko, who is highly ...</p>
      <span class="btn">Read More</span>
    </div>
    <div class="card">
      <div class="photo" role="img" aria-label="Lawyers reviewing documents in a meeting" style="background:linear-gradient(135deg,#8aa0b8,#2c3c52)"></div>
      <h3>Commercial Litigation</h3>
      <p>We have a reputation for producing excellent results for our litigation clients. Since 1966, the firm has ...</p>
      <span class="btn on">Read More</span>
    </div>
    <div class="card">
      <div class="photo" role="img" aria-label="Parties negotiating at a conference table" style="background:linear-gradient(135deg,#c9ccd2,#4a5260)"></div>
      <h3>Arbitration</h3>
      <p>We advise clients on both domestic and international arbitration proceedings and other forms of ...</p>
      <span class="btn">Read More</span>
    </div>
  </div>
</section>

<section class="how">
  <div class="label">Mbeleko &amp; Tumusiime</div>
  <h2 class="title">How We Do it</h2>
  <div class="values">
    <div class="value">
      <div class="ring"><svg width="40" height="36" viewBox="0 0 40 36"><path d="M20 3v28M8 31h24M6 8h28M6 8l-5 12h10zM34 8l-5 12h10z" fill="none" stroke="#b31b2c" stroke-width="2"/></svg></div>
      <h3>Integrity</h3>
      <p>We maintain ethical behaviour and strict moral values. We are honest and trustworthy in our dealings with ...</p>
    </div>
    <div class="value">
      <div class="ring on"><svg width="40" height="30" viewBox="0 0 40 30"><path d="M2 12l8-8 8 4 6-4 14 10-12 10-8-6-6 4z" fill="none" stroke="#fff" stroke-width="2.5" stroke-linejoin="round"/></svg></div>
      <h3>Partnership</h3>
      <p>We partner with our clients and keep a close and interactive relationship that enriches our business ...</p>
    </div>
    <div class="value">
      <div class="ring"><svg width="38" height="38" viewBox="0 0 38 38"><circle cx="19" cy="19" r="7" fill="none" stroke="#b31b2c" stroke-width="2"/><circle cx="19" cy="19" r="14" fill="none" stroke="#b31b2c" stroke-width="4" stroke-dasharray="5 4"/></svg></div>
      <h3>Efficiency</h3>
      <p>We work to surpass our clients' expectations. We are practical and solution driven in our approach ...</p>
    </div>
  </div>
  <div class="how-rule"></div>
  <span class="btn">Free Consultation</span>
</section>

<section class="clients">
  <h2 class="title">Our Clients</h2>
  <div class="tabs"><span>Commercial Litigation &amp; Transactions</span><span class="on">Construction &amp; Arbitration</span><span>Corporate Advisory</span></div>
  <svg style="position:absolute;left:146px;top:218px" width="10" height="18" viewBox="0 0 10 18"><path d="M8 1 1 9l7 8" fill="none" stroke="#555" stroke-width="2"/></svg>
  <div class="logos">
    <div class="logo">NORVA</div>
    <div class="logo">BRIXTEL</div>
    <div class="logo on">KALDEN</div>
    <div class="logo">TAXCO</div>
    <div class="logo">UMARA</div>
  </div>
  <svg style="position:absolute;left:1046px;top:218px" width="10" height="18" viewBox="0 0 10 18"><path d="M2 1l7 8-7 8" fill="none" stroke="#555" stroke-width="2"/></svg>
</section>

<section class="team">
  <div class="label">Mbeleko &amp; Tumusiime Team</div>
  <h2 class="title">Our Professionals</h2>
  <svg style="position:absolute;left:124px;top:290px" width="8" height="14" viewBox="0 0 8 14"><path d="M7 1 1 7l6 6" fill="none" stroke="#b31b2c" stroke-width="2"/></svg>
  <div class="members">
    <div class="member"><div class="photo" role="img" aria-label="Portrait of the managing partner"></div><div class="info"><h4>Joseph K. Mbeleko</h4><span>Managing Partner</span></div></div>
    <div class="member on"><div class="photo" role="img" aria-label="Portrait of the senior partner"></div><div class="info"><h4>Daniel S. Mbeleko</h4><span>Senior Partner</span></div></div>
    <div class="member"><div class="photo" role="img" aria-label="Portrait of the head of litigation"></div><div class="info"><h4>Samuel Okello</h4><span>Head of Litigation</span></div></div>
    <div class="member"><div class="photo" role="img" aria-label="Portrait of the head of business development"></div><div class="info"><h4>Nathan Kirabo</h4><span>H. of Business Development</span></div></div>
  </div>
  <svg style="position:absolute;left:1068px;top:290px" width="8" height="14" viewBox="0 0 8 14"><path d="M1 1l6 6-6 6" fill="none" stroke="#b31b2c" stroke-width="2"/></svg>
  <span class="btn">View All Team</span>
</section>

<section class="contact">
  <div class="eyebrow">Contact Us</div>
  <h2 class="title">Get In Touch</h2>
  <div class="info-col">
    <h3>Contact Info</h3>
    <h4>Address</h4>
    <p>Plot 14, Kiira Road<br>2nd Floor, Rwenzori Court P.O Box 7731,<br>Kampala, Uganda.</p>
    <h4>Call Today</h4>
    <p style="font-size:16px">0414 555 018</p>
    <h4>Email</h4>
    <p>info@mtadvocates.example</p>
  </div>
  <div class="form-col">
    <h3>Write a Message</h3>
    <div class="fields"><div class="field">Name</div><div class="field">Email</div><div class="field">Phone</div></div>
    <div class="area">Tell us about your case...</div>
    <span class="btn">Send</span>
  </div>
</section>

<section class="map" role="img" aria-label="Street map showing the office location in Kampala"></section>

<footer class="site-footer">
  <div class="brand">
    <div class="brand-square"></div>
    <div class="brand-name">Mbeleko &amp; Tumusiime Advocates</div>
  </div>
  <nav class="foot-nav">
    <span class="active">Home</span><span>Our History</span><span>Who We Are</span><span>How We Do It</span><span>Practice Areas</span><span>Our clients</span><span>Our Professionals</span><span>Contact Us</span>
  </nav>
  <div class="foot-bottom">
    <span>© 2016 Mbeleko &amp; Tumusiime Advocates. All Right Reserved</span>
    <span class="social">Get Social <i></i><i></i><i></i><i></i></span>
  </div>
</footer>

</body>
</html>
```